Kestrafab, NSW. Manufacturing/Construction industry. Require 4 page brochure/flyer

www.kestrafab.com.au - see website for branding/colours
Require a double sided A3 folded - so 4 x A4 page brochure on the company to provide to potential clients showcasing our capabilities.
I have an idea what I would like, but am not a graphic designer so struggle with making it look attractive.
Page 1: Photo of shed steelwork + logo, company name etc
Page 2: Who we are, where we are, capabilities and technological advantages
Page 3: What we do, what we will do for the new client
Page 4: Photo with contact details
I dont mind if the designer can create the basic design and can fill in the details later once the design is finalised.
Have uploaded some basic photos similar to what I could use, however they are low quality so would need higher resolution. Also uploaded a basic flyer we currently use to show previously completed projects just for information.

Target Market(s)

Developers

Industry/Entity Type

Manufacturing

Font styles to use
Other font styles liked:
• OpenSans

Colors
0355a3
3377b5
85acd3

Requirements
Must have
• 4 x A4 pages, pages 2 and 3 to be A3 size, so flow together.
Nice to have
• Have attached capability brochure that we currently use. The new one will need to be similar level of professionalism, however less words/details

```html
<!DOCTYPE html>
<html lang="en">
<head>
<meta charset="utf-8">
<title>Kestrafab Capability Brochure</title>
<link href="https://fonts.googleapis.com/css2?family=Open+Sans:wght@400;600;700;800&display=swap" rel="stylesheet">
<style>
:root{
  --navy:#1d4474;
  --navy-deep:#163a66;
  --brand:#0355a3;
  --mid:#3377b5;
  --sky:#5cc3ee;
  --pale:#85acd3;
  --ink:#2a2f38;
  --paper:#ffffff;
  --stage:#dedede;
}
*{box-sizing:border-box;margin:0;padding:0}
html,body{width:1200px;height:4000px;overflow:hidden;background:var(--stage);font-family:"Open Sans",Arial,sans-serif;color:var(--ink)}
.spread{position:absolute;left:50px;width:1100px;height:778px;background:var(--paper);box-shadow:0 10px 30px rgba(0,0,0,.18);overflow:hidden}
.spread--outer{top:1130px}
.spread--inner{top:2070px}
.spread svg.shapes{position:absolute;left:0;top:0}
.abs{position:absolute}
.brand{display:flex;align-items:center;gap:10px;color:#fff;font-weight:800;letter-spacing:.5px}
.brand__dot{border-radius:50%;background:#fff}
.cover-brand{left:640px;top:505px;font-size:26px}
.cover-brand .brand__dot{width:52px;height:52px}
.back-brand{left:52px;top:662px;font-size:17px}
.back-brand .brand__dot{width:38px;height:38px}
.cover-title{left:550px;width:550px;top:612px;text-align:center;color:#fff;font-weight:700;font-size:23px;line-height:29px;letter-spacing:.3px}
.cover-title .pill{display:inline-block;background:var(--sky);border-radius:16px;padding:0 18px;margin-top:3px}
.cover-url{left:550px;width:550px;top:742px;text-align:center;color:#fff;font-size:12px;font-weight:600;letter-spacing:1.5px}
.contact{left:292px;top:596px;color:#fff;font-size:12.5px;line-height:17px}
.contact h4{color:var(--sky);font-size:11px;font-weight:700;text-decoration:underline;margin-bottom:3px}
.photo{position:absolute}
.h2{font-weight:700;font-size:15px;color:var(--navy);letter-spacing:.3px}
.body{font-size:7.4px;line-height:10px;color:#333}
.body p{margin-bottom:5px}
.body b{color:var(--brand)}
.who{left:46px;top:40px;width:470px}
.where-title{left:46px;top:302px}
.cap-table{position:absolute;left:46px;top:324px;width:470px;border-collapse:collapse;font-size:7px}
.cap-table th{background:var(--navy);color:#fff;text-align:left;padding:3px 8px;font-weight:700}
.cap-table td{padding:2px 8px;height:14.4px;border-bottom:1px solid #e5e8ee}
.cap-table tr:nth-child(even) td{background:#f1f4f8}
.cap-table td:first-child{width:34%}
.caps{left:46px;top:650px;width:240px}
.caps h3{color:var(--navy);font-size:15px;line-height:17px;font-weight:600}
.caps p{font-size:7.5px;line-height:10px;color:var(--navy-deep);margin-top:4px}
.inner-url{left:46px;top:744px;font-size:9.5px;color:var(--navy);letter-spacing:1px}
.what-title{left:584px;top:40px}
.col{top:66px;width:220px}
.col1{left:584px}
.col2{left:836px}
.col h5{font-size:7px;font-weight:700;color:var(--navy);margin-top:6px}
.col h6{font-size:7px;font-weight:400;color:#444;margin-bottom:4px}
</style>
</head>
<body>

<!-- Outer spread: back cover (left) + front cover (right) -->
<section class="spread spread--outer" aria-label="Outer spread: back and front cover">
  <svg class="shapes" width="1100" height="778" viewBox="0 0 1100 778">
    <defs>
      <linearGradient id="stairs" x1="0" y1="0" x2="1" y2="1">
        <stop offset="0" stop-color="#f7f8fa"/><stop offset="1" stop-color="#dfe3e8"/>
      </linearGradient>
      <linearGradient id="factory" x1="0" y1="0" x2="0" y2="1">
        <stop offset="0" stop-color="#3a4a52"/><stop offset=".45" stop-color="#6f7c78"/><stop offset="1" stop-color="#8a8f8e"/>
      </linearGradient>
    </defs>
    <rect x="0" y="0" width="550" height="600" fill="url(#stairs)" role="img" aria-label="Faint photo of white steel staircase"/>
    <polygon points="550,0 1100,0 1100,380 550,475" fill="url(#factory)" role="img" aria-label="Photo of steel fabrication workshop interior"/>
    <polygon points="0,450 390,520 0,588" fill="var(--sky)"/>
    <polygon points="0,586 1100,396 1100,410 0,600" fill="#fff"/>
    <polygon points="0,600 1100,410 1100,778 0,778" fill="var(--navy)"/>
    <polygon points="550,476 1100,382 1100,388 550,482" fill="var(--mid)"/>
    <rect x="63" y="308" width="132" height="132" fill="#6b5a4a" role="img" aria-label="Photo of timber and steel stair"/>
    <rect x="209" y="308" width="132" height="132" fill="#8a8e90" role="img" aria-label="Photo of steel stair frame in building"/>
    <rect x="354" y="308" width="132" height="132" fill="#a8855a" role="img" aria-label="Photo of walkway with yellow handrails"/>
  </svg>
  <div class="abs brand back-brand"><span class="brand__dot"></span>KESTRAFAB</div>
  <div class="abs contact">
    <h4>CONTACT US</h4>
    48 Harlow Rd<br>PO Box 512<br>Berrima Vale NSW 2580<br><br>
    P: (02) 5550 1840<br>F: (02) 5550 1842<br>E: estimator@kestrafab.com.au<br>W: www.kestrafab.com.au
  </div>
  <div class="abs brand cover-brand"><span class="brand__dot"></span>KESTRAFAB</div>
  <div class="abs cover-title">A LEADING STEEL FABRICATION<br>BUSINESS WITH<br><span class="pill">50 YEARS OF EXPERIENCE</span></div>
  <div class="abs cover-url">www.kestrafab.com.au</div>
</section>

<!-- Inner spread: pages 2 and 3 -->
<section class="spread spread--inner" aria-label="Inner spread: who we are and what we do">
  <svg class="shapes" width="1100" height="778" viewBox="0 0 1100 778">
    <defs>
      <linearGradient id="site" x1="0" y1="0" x2="0" y2="1">
        <stop offset="0" stop-color="#4f86c6"/><stop offset=".55" stop-color="#9fb6c8"/><stop offset="1" stop-color="#c9b89a"/>
      </linearGradient>
    </defs>
    <polygon points="0,600 1100,380 1100,404 0,624" fill="var(--navy)"/>
    <polygon points="0,628 1100,408 1100,412 0,632" fill="var(--mid)"/>
    <polygon points="0,632 550,522 550,778 0,778" fill="var(--sky)"/>
    <polygon points="550,522 1100,412 1100,778 550,778" fill="var(--navy)"/>
    <polygon points="560,560 1100,452 1100,778 560,778" fill="url(#site)" role="img" aria-label="Photo of steel shed frame under construction on site"/>
    <rect x="293" y="598" width="106" height="72" fill="#7b8792" role="img" aria-label="Project photo of steel frame"/>
    <rect x="403" y="598" width="106" height="72" fill="#8b7560" role="img" aria-label="Project photo of workshop"/>
    <rect x="293" y="674" width="106" height="72" fill="#6d7a66" role="img" aria-label="Project photo of site steelwork"/>
    <rect x="403" y="674" width="106" height="72" fill="#a3acb4" role="img" aria-label="Project photo of staircase"/>
  </svg>

  <h2 class="abs h2" style="left:46px;top:20px">WHO WE ARE</h2>
  <div class="abs body who">
    <p>In 1964 the Harlow family started making simple steel products for the local farmers in the Southern Highlands of NSW. Today, over 50 years later, it is still operated by the family. Kestrafab has become a highly respected steel fabrication business with a large well-equipped workshop in Berrima Vale NSW. We have completed many of major steel construction projects for leading builders and architects and are at the forefront of prefabricated stairway design for large multistorey buildings.</p>
    <p><b>INNOVATION</b> We simplify the steelwork of complex and detailed architect plans to reduce costs and overall build times. Our in-house capabilities allow us to provide time effective and on budget turn-key solutions for our clients.</p>
    <p><b>COMMITMENT</b> We have an excellent reputation throughout the industry for delivering quality work and having the advantage of our onsite workshop means we also deliver on time and on budget. Our team's expertise and capabilities give assurance to clients for any project, regardless of size or complexity. Being Industry Environmental Sustainability Charter compliant and ISO qualified along with ongoing internal training and development, we consistently contribute to maintaining our highly regarded position within our industry.</p>
    <p><b>PRECISION</b> With in-house state of the art technology and systems in place, we can produce outstanding quality work with precision. Our workshop has the capability to produce high-level detailed drawings and 3D modelling. Our Robotic Beam Line and Plasma Cutter ensures that we produce the most accurate steelwork.</p>
  </div>
  <h2 class="abs h2 where-title">WHERE WE ARE</h2>
  <table class="cap-table">
    <thead><tr><th>Capability</th><th>Builder benefits</th></tr></thead>
    <tbody>
      <tr><td>Problem Solving</td><td>Structural steel solutions for architecturally complex multi-storey buildings</td></tr>
      <tr><td>Project Management</td><td>Experienced full time project managers on-site</td></tr>
      <tr><td>Workshop Drafting</td><td>Workshop plans and 3D drafting with BIM and 3D modelling software</td></tr>
      <tr><td>Structural Steelwork</td><td>For the most architecturally complex buildings</td></tr>
      <tr><td>Multi Story Inner City Buildings</td><td>Complex high rise buildings and refurbishment projects</td></tr>
      <tr><td>Stairway Build Systems</td><td>Modular stair way build systems that dramatically reduce cycle times</td></tr>
      <tr><td>Designer Feature Stairways</td><td>Design and function combine to make stunning feature stairways</td></tr>
      <tr><td>Facade Steelwork</td><td>Detailed precision steelwork for large building facades</td></tr>
      <tr><td>High Volume Precision Steelwork</td><td>Large beam line with in-line blasting</td></tr>
      <tr><td>Workshop Assembly</td><td>Assembly of key components before delivery to the building site</td></tr>
      <tr><td>Surface Preparation</td><td>In-line blasting, sealing and painting prior to delivery</td></tr>
      <tr><td>Construction &amp; Rigging</td><td>Experienced team of on-site riggers</td></tr>
      <tr><td>Environmental Compliance</td><td>Industry Environmental Sustainability Charter compliant</td></tr>
      <tr><td>ISO accredited</td><td>All work exceeds Australian quality standards</td></tr>
    </tbody>
  </table>
  <div class="abs caps">
    <h3>CAPABILITIES AND<br>TECHNOLOGICAL ADVANTAGES</h3>
    <p>Large and complex projects can be completed totally in-house<br>Design | Manage | Fabricate | Build</p>
  </div>
  <div class="abs inner-url">www.kestrafab.com.au</div>

  <h2 class="abs h2 what-title">WHAT WE DO</h2>
  <div class="abs body col col1">
    <h5>STRUCTURAL STEELWORK</h5>
    <h6>Kestrafab specialise in large complex structural steel projects.</h6>
    <h5>PRECISION | HIGH VOLUME | QUICK TURNAROUND</h5>
    <p>Our workshop has been designed to produce high volumes of fabricated structural steel with short turnarounds. The CNC Beam Line is used to produce large volumes of fabricated structural steel with rapid turnaround times. Workshop drawings are produced in-house to provide detailed 3D work plans. We have a team of full time supervised and skilled staff. To improve build quality and reduce build times we can construct key components of the steelwork in the workshop and crane them into position onsite. We have a team of skilled construction and rigging staff who undertake the onsite build with speed and precision.</p>
    <h5>FACADE STEELWORK</h5>
    <h6>Kestrafab provide steelwork for all types of facades</h6>
    <h5>PRECISION | DETAILED STEELWORK</h5>
    <p>Kestrafab have the expertise and workshop capabilities to produce the complex and detailed steelwork required to fix the facades on large multistorey buildings. Kestrafab can also produce the steelwork necessary to support the large areas of glass panelling used in multi-storey office buildings and retail complexes. To improve build quality and reduce build times we can construct key components of the steelwork in the workshop and crane them into position onsite. We have a team of skilled construction and rigging staff who undertake the onsite build with speed and precision.</p>
  </div>
  <div class="abs body col col2">
    <h5>WEATHERING STEEL</h5>
    <h6>Kestrafab has the expertise and equipment to work with weathering steel</h6>
    <h5>STRUCTURAL STEEL | FABRICATE | INSTALL</h5>
    <p>Weathering steel provides a dramatic weathered steel appearance to landmark buildings. Kestrafab have had extensive experience in working with weathering steel. We work with architects to simplify the structural steel frames used to support the weathering steel sheets. We can fabricate structures in weathering steel. We have a team of skilled construction and rigging staff who can install weathering steel with speed and precision.</p>
    <h5>SHADING AND SCREENING</h5>
    <h6>Kestrafab specialise in the most architecturally complex and detailed designs</h6>
    <h5>SCREENS | SHADING | AWNINGS | PERGOLAS | LOUVRES</h5>
    <p>Architecturally designed pergolas, awnings and screens are features that can add function and beauty. Kestrafab have had extensive experience in fabricating and installing complex architectural features for major projects. We have the 3D modelling capability to translate architecturally complex designs into simplified workshop drawings. Our experienced team of workshop staff have the detailed precision steelwork skills to bring the architects concept to life.</p>
  </div>
</section>

</body>
</html>
```